Innovative WordPress for a non-profit organization dedicated to providing healthcare to the less for

Bright Harbor Aid is a small non-profit organization. BHA's core mission is to provide free medical and dental care to the less fortunate. Aside from providing healthcare, BHA also helps build infrastructure such as orphanage, cancer centers, water wells and small homes for the homeless. As a non-profit, BHA has been sponsoring various social programs to help those in need. From building infrastructure to health care and most recently micro-finance, the BHA team is helping to GIve Back to the community at person at a time.

BHA is growing and needs help to restructure for the future. The corporate website design is the first step in a new branding strategy for the company.

BHA current website is divided into three specific target areas:
1. Mission: This area is dedicated to provide information about medical and dental mission hosted by BHA.

2. Infrastructure. This area is dedicated to provide information about infrastructure programs supported and completed by the BHA team. The projects includes orphanage, cancer centers. water wells, micro-finance, small homes for the homeless...etc.

3. Special Projects. This area is used to showcase specific short term projects which might come up.

Aside from the specific three target area, BHA also needs a NEWS area where news about BHA can be published.

Please put your thinking cape on and help produce the next generation WordPress template for Bright Harbor Aid. Your design will great enhance the level of volunteers recruited and also increase the level of help that BHA can provide for other.

For a quick glance at the BHA website today, please visit http://www.bhaexample.org. The BHA team is looking for a fresh design.

Thank you very much for taking the time to help BHA advance its mission of helping those in need.

Reason: Seeking more variety in design. Design needs to have a donate button, sponsors area, news, welcome message, 3 primary functions (mission, infrastructure, and specials projects). The BHA logo is available. Please note, you have the option to NOT use the colors associated with BHA logo. Thank you for helping with designing the new site.

Non-Profit

Requirements
Must have
• 1. Donate Now button.
2. Primary focus areas: MISSION / INFRASTRUCTURE / SPECIAL PROJECTS
3. News & Events
4. Welcome Message area
5. Sponsors area - place to add sponsor logos

Nice to have
• 1. Photo of the Month: Used to show a specific photo to represent events or functions completed by the BHA team.

Please show sample of one level down. For example, what does the page look like when I click the MISSION link.

```html
<!DOCTYPE html>
<html lang="en">
<head>
<meta charset="utf-8">
<title>Bright Harbor Aid</title>
<link href="https://fonts.googleapis.com/css2?family=Open+Sans:wght@400;600;700;800&display=swap" rel="stylesheet">
<style>
:root{
  --blue:#1e73be;
  --blue-dark:#155a96;
  --navy:#0f3e6b;
  --ink:#333a40;
  --muted:#7a8288;
  --line:#dde1e4;
  --page:#eef0f2;
  --white:#ffffff;
  --footer:#e3e5e7;
  --bottom:#2c3136;
}
*{box-sizing:border-box;margin:0;padding:0}
html,body{width:837px;height:1200px;overflow:hidden}
body{font-family:"Open Sans",Arial,sans-serif;background:var(--page);color:var(--ink);font-size:8px;line-height:1.5;position:relative}
.wrap{position:absolute;left:40px;width:757px}
.header{top:0;height:50px;background:var(--white);display:flex;align-items:center;justify-content:space-between;padding:0 14px}
.logo{display:flex;align-items:center;gap:6px;font-weight:800;font-size:17px;color:var(--blue)}
.logo .mark{width:16px;height:16px;background:var(--blue)}
.logo small{font-size:7px;font-weight:600;color:var(--blue);display:block;line-height:1}
.contact{display:flex;gap:14px;font-size:7.5px;color:var(--muted)}
.contact span{display:flex;align-items:center;gap:4px}
.nav{top:50px;height:30px;background:var(--blue);display:flex;align-items:center;padding:0 14px;gap:4px}
.nav a{color:var(--white);text-decoration:none;font-size:8.5px;font-weight:600;padding:0 10px;height:30px;line-height:30px}
.nav a.active{background:var(--blue-dark)}
.nav .donate{margin-left:auto;background:#f3a01b;border-radius:3px;height:20px;line-height:20px}
.hero{top:80px;height:185px;background:linear-gradient(100deg,#5b6b74 0%,#8b8d86 45%,#c9c4ba 70%,#8e9aa1 100%)}
.hero .caption{position:absolute;left:120px;top:70px;width:260px;color:var(--white);text-align:center}
.hero h1{font-size:15px;font-weight:800;line-height:1.3}
.hero p{font-size:7.5px;margin-top:4px}
.panel{top:265px;height:1070px;background:var(--white)}
.focus{position:absolute;top:-60px;left:0;width:757px;display:flex;justify-content:space-around;padding:0 50px}
.focus-item{width:170px;text-align:center}
.circle{width:96px;height:96px;border-radius:50%;background:var(--blue);border:5px solid var(--white);margin:0 auto;display:flex;align-items:center;justify-content:center}
.focus-item h2{font-size:10px;font-weight:700;color:var(--ink);margin-top:6px;letter-spacing:.3px}
.focus-item p{font-size:6.5px;color:var(--muted);margin-top:4px}
.btn{display:inline-block;background:var(--blue);color:var(--white);font-size:7px;padding:3px 12px;border-radius:2px;margin-top:7px}
.main{position:absolute;left:14px;top:172px;width:570px}
.main h3{font-size:13px;font-weight:700;color:var(--ink);border-bottom:1px solid var(--line);padding-bottom:3px;margin-bottom:6px}
.main p{font-size:6.5px;color:var(--muted);margin-bottom:5px}
.photos{display:flex;gap:8px;margin-top:4px}
.photos figure{flex:1}
.photos .ph{height:80px;background:linear-gradient(135deg,#8a9aa6,#c3b9a9)}
.photos figcaption{font-size:6px;color:var(--muted);margin-top:2px}
.dots{display:flex;gap:4px;justify-content:center;margin:8px 0 12px}
.dots i{width:5px;height:5px;border-radius:50%;background:#c7ccd0}
.dots i.on{background:var(--blue)}
.sponsors{display:flex;gap:14px;align-items:center;justify-content:space-between;padding:10px 4px}
.sponsors span{background:#dfe4e8}
.side{position:absolute;left:600px;top:172px;width:145px}
.side h4{background:var(--blue);color:var(--white);font-size:9px;font-weight:700;padding:4px 8px}
.news li{list-style:none;display:flex;gap:6px;padding:6px 4px;border-bottom:1px solid var(--line)}
.news .th{width:26px;height:22px;background:linear-gradient(135deg,#7f93a3,#b9ad9c);flex:none}
.news b{font-size:6.5px;display:block;color:var(--ink)}
.news small{font-size:6px;color:var(--blue)}
.map{height:130px;background:linear-gradient(135deg,#e9ecdf,#dfe6ee);margin-top:6px}
.footer{top:920px;height:195px;background:var(--footer);padding:18px 20px;display:flex;gap:30px}
.footer h5{font-size:11px;font-weight:700;color:var(--ink);margin-bottom:6px}
.footer p{font-size:6.5px;color:var(--muted);margin-bottom:5px}
.f-about{width:460px}
.social{display:flex;gap:22px;margin-top:6px}
.social span{display:flex;align-items:center;gap:5px;font-size:6.5px;color:var(--muted)}
.social i{width:18px;height:18px;border-radius:50%;background:var(--blue)}
.f-offers{flex:1}
.field{height:16px;background:var(--white);border:1px solid var(--line);margin:5px 0}
.bottom{top:1115px;height:85px;background:var(--bottom);color:#aab1b7;font-size:6.5px;display:flex;justify-content:space-between;padding:10px 20px}
</style>
</head>
<body>
<header class="wrap header">
  <div class="logo"><span class="mark"></span><div>BHA<small>Bright Harbor Aid</small></div></div>
  <div class="contact">
    <span><svg width="8" height="8" viewBox="0 0 10 10"><path d="M2 1l2 2-1 1.5c.6 1.2 1.3 1.9 2.5 2.5L7 6l2 2-1.5 1.5C4 9 1 6 .5 2.5z" fill="#1e73be"/></svg>(555) 014-2290</span>
    <span><svg width="8" height="8" viewBox="0 0 10 10"><path d="M5 0a3.5 3.5 0 0 0-3.5 3.5C1.5 6 5 10 5 10s3.5-4 3.5-6.5A3.5 3.5 0 0 0 5 0z" fill="#1e73be"/></svg>120 Harbor Lane, Suite 4</span>
    <span><svg width="9" height="7" viewBox="0 0 10 8"><rect width="10" height="8" fill="#1e73be"/><path d="M0 0l5 4 5-4" stroke="#fff" fill="none"/></svg>hello@bhaexample.org</span>
  </div>
</header>
<nav class="wrap nav">
  <a class="active">Home</a><a>About Us</a><a>Mission</a><a>Special Projects</a><a>Infrastructure</a><a>Events</a>
  <a class="donate">Donate Now</a>
</nav>
<section class="wrap hero" role="img" aria-label="Photo of volunteer dentists treating a patient at a free dental clinic">
  <div class="caption">
    <h1>Dr. Lien Tran and Dr. Minh Vo at BHA hosted free Dental Clinic.</h1>
    <p>Our dental team offered free checkups and treatment to local families this spring.</p>
  </div>
</section>
<main class="wrap panel">
  <div class="focus">
    <div class="focus-item">
      <div class="circle"><svg width="40" height="40" viewBox="0 0 40 40" fill="#fff"><rect x="6" y="14" width="12" height="22"/><rect x="20" y="6" width="14" height="30"/><g fill="#1e73be"><rect x="9" y="18" width="3" height="3"/><rect x="13" y="18" width="3" height="3"/><rect x="9" y="24" width="3" height="3"/><rect x="13" y="24" width="3" height="3"/><rect x="23" y="10" width="3" height="3"/><rect x="28" y="10" width="3" height="3"/><rect x="23" y="16" width="3" height="3"/><rect x="28" y="16" width="3" height="3"/><rect x="23" y="22" width="3" height="3"/><rect x="28" y="22" width="3" height="3"/></g></svg></div>
      <h2>INFRASTRUCTURE</h2>
      <p>We help build orphanages, cancer centers, water wells and small homes for families who need shelter and care.</p>
      <span class="btn">Read More</span>
    </div>
    <div class="focus-item">
      <div class="circle"><svg width="36" height="40" viewBox="0 0 36 40"><path d="M8 4c5 0 7 3 10 3s5-3 10-3c6 0 8 6 6 13-2 6-3 12-5 18-1 3-4 3-5 0l-2-8c-1-3-3-3-4 0l-2 8c-1 3-4 3-5 0C9 29 8 23 6 17 4 10 3 4 8 4z" fill="#fff"/></svg></div>
      <h2>MISSION</h2>
      <p>Through our yearly medical and dental missions we bring free care to those who could not reach it otherwise.</p>
      <span class="btn">Read More</span>
    </div>
    <div class="focus-item">
      <div class="circle"><svg width="44" height="36" viewBox="0 0 44 36" fill="#fff"><circle cx="22" cy="8" r="6"/><path d="M12 30c0-7 4-12 10-12s10 5 10 12z"/><circle cx="9" cy="12" r="4.5"/><path d="M1 32c0-6 3-10 8-10s8 4 8 10z"/><circle cx="35" cy="12" r="4.5"/><path d="M27 32c0-6 3-10 8-10s8 4 8 10z"/></svg></div>
      <h2>SPECIAL PROJECTS</h2>
      <p>Short term projects that come up, from micro-finance loans to emergency relief for a village in need.</p>
      <span class="btn">Read More</span>
    </div>
  </div>

  <div class="main">
    <h3>Welcome Message area</h3>
    <p>Bright Harbor Aid is a small non-profit team of doctors, dentists and volunteers who share one goal: giving free medical and dental care to the less fortunate. Since our first clinic we have treated thousands of patients and grown our reach to new towns every year. Our volunteers give their time, skill and heart to make each mission count.</p>
    <p>Beyond health care we build lasting help: orphanages, cancer centers, clean water wells and homes for the homeless. Most recently we began a micro-finance program that helps families start small businesses. Join us and help give back to the community, one person at a time.</p>
    <h3 style="margin-top:10px">Photo of the Month</h3>
    <div class="photos">
      <figure><div class="ph" role="img" aria-label="Photo of a mission clinic"></div><figcaption>Lorem ipsum</figcaption></figure>
      <figure><div class="ph" role="img" aria-label="Photo of volunteers at work"></div><figcaption>Lorem ipsum</figcaption></figure>
      <figure><div class="ph" role="img" aria-label="Photo of a new water well"></div><figcaption>Lorem ipsum</figcaption></figure>
      <figure><div class="ph" role="img" aria-label="Photo of children at an orphanage"></div><figcaption>Lorem ipsum</figcaption></figure>
    </div>
    <div class="dots"><i class="on"></i><i></i><i></i></div>
    <h3>Sponsors Area</h3>
    <div class="sponsors">
      <span style="width:60px;height:60px;border-radius:50%"></span>
      <span style="width:40px;height:60px"></span>
      <span style="width:120px;height:50px"></span>
      <span style="width:60px;height:60px;border-radius:50%"></span>
      <span style="width:120px;height:40px"></span>
    </div>
    <div class="dots"><i class="on"></i><i></i><i></i></div>
  </div>

  <aside class="side">
    <h4>News &amp; Events</h4>
    <ul class="news">
      <li><div class="th" role="img" aria-label="News photo"></div><div><b>Spring dental clinic opens</b><small>Read more</small></div></li>
      <li><div class="th" role="img" aria-label="News photo"></div><div><b>New well serves two villages</b><small>Read more</small></div></li>
      <li><div class="th" role="img" aria-label="News photo"></div><div><b>Volunteers wanted this fall</b><small>Read more</small></div></li>
      <li><div class="th" role="img" aria-label="News photo"></div><div><b>Micro-finance update</b><small>Read more</small></div></li>
      <li><div class="th" role="img" aria-label="News photo"></div><div><b>Orphanage roof completed</b><small>Read more</small></div></li>
      <li><div class="th" role="img" aria-label="News photo"></div><div><b>Annual gala a success</b><small>Read more</small></div></li>
      <li><div class="th" role="img" aria-label="News photo"></div><div><b>Cancer center milestone</b><small>Read more</small></div></li>
    </ul>
    <h4 style="margin-top:14px">Our Location</h4>
    <div class="map" role="img" aria-label="Street map showing the office location"></div>
  </aside>
</main>
<footer class="wrap footer">
  <div class="f-about">
    <h5>About Us</h5>
    <p>Bright Harbor Aid brings free medical and dental care to people in need and helps build the places that keep communities healthy. Every gift and every hour given makes the next mission possible.</p>
    <p>Read more about our story, our team and the projects we support at home and abroad.</p>
    <h5 style="margin-top:10px">Connect With Us</h5>
    <div class="social"><span><i></i>Like us online</span><span><i></i>Follow our updates</span><span><i></i>Join our network</span></div>
  </div>
  <div class="f-offers">
    <h5>Get Special Offers</h5>
    <p>Subscribe to our newsletter for news and event updates.</p>
    <div class="field"></div>
    <span class="btn" style="margin-top:0">Subscribe</span>
  </div>
</footer>
<div class="wrap bottom">
  <span>© 2024 Bright Harbor Aid. All rights reserved.</span>
  <span>Home | About Us | Mission | Special Projects | Infrastructure | Events</span>
</div>
</body>
</html>
```